DESIGN A ALL CROWD PULLER A CATCHY NIGHT CLUBB FLYER.Ngoma is simple a drum...Include A beautiful African girl with a A-FRO AND A DRUM

Target Market(s)

NIGHT CLUBB GOERS

Industry/Entity Type

Crowd

Requirements
Must have
• launching:TV-VELDA RUSHO

HOUSE PARTY!

Bored & feeling like grooving to Funkhouse.Dance. Dubstep.Electro.Afro beat.
R n B,Hip Hop.Dancehall. Reggae.Raggaeton. Zouk.Live bands & Poerty

Velda Rusho is the place to be

Friday the 16th Jan. 2015 9pm-3am
& every second Friday of the month

@ TOLM Prins Halvard gate 42,5032 Bergen

AGE:18+ KR 100

New Year, New Klubb,New City vibes & sounds!!

For more information visit our site
www.lorenvisuals.org fb-veldarusho

DRINKS & FOOD SAVED ON CASH ONLY!!
Nice to have
• Add a African girl with a Afro and DRUM

```html
<!DOCTYPE html>
<html lang="en">
<head>
<meta charset="utf-8">
<title>Velda Rusho House Party Flyer</title>
<link rel="stylesheet" href="https://fonts.googleapis.com/css2?family=Great+Vibes&family=Raleway:wght@300;400;600;700;800&display=swap">
<style>
  :root {
    --ink: #0c0a0c;
    --white: #ffffff;
    --magenta: #e81fd0;
    --hot-pink: #ff2ab8;
    --deep-pink: #c01aa8;
    --plum: #3a0c42;
    --violet-shadow: #5a1060;
    --wine: #8a0f30;
    --wine-deep: #5e0a22;
  }
  * { margin: 0; padding: 0; box-sizing: border-box; }
  html, body { width: 849px; height: 1200px; overflow: hidden; background: var(--white); }
  .flyer {
    position: relative; width: 849px; height: 1200px; overflow: hidden;
    font-family: "Raleway", sans-serif; background: var(--white);
  }
  .launch-band {
    position: absolute; left: 0; top: 0; width: 849px; height: 134px;
    background: var(--ink); display: flex; align-items: center; justify-content: center;
    gap: 10px; padding-bottom: 6px;
  }
  .launch-label { color: var(--white); font-size: 29px; font-weight: 500; }
  .launch-name { color: var(--magenta); font-size: 36px; font-weight: 800; letter-spacing: 0.5px; }

  .stage {
    position: absolute; left: 0; top: 148px; width: 849px; height: 898px;
    background: radial-gradient(ellipse at 60% 30%, #f43ee0 0%, #e024c8 45%, #c816b2 100%);
  }
  .crowd-photo { position: absolute; inset: 0; }
  .drummer-art { position: absolute; left: 18px; top: 180px; width: 440px; height: 718px; }

  .headline {
    position: absolute; left: 62px; top: 158px; width: 760px;
    font-family: "Great Vibes", cursive; font-size: 138px; line-height: 1;
    color: var(--white); transform: rotate(-4deg);
    text-shadow: 3px 3px 0 var(--violet-shadow), -1px -1px 0 var(--violet-shadow), 1px -1px 0 var(--violet-shadow), -1px 1px 0 var(--violet-shadow);
  }
  .tagline {
    position: absolute; left: 400px; top: 370px;
    color: var(--ink); font-size: 27px; font-weight: 700; line-height: 36px;
  }
  .genres {
    position: absolute; left: 290px; top: 473px; width: 530px;
    color: var(--white); font-size: 25.5px; font-weight: 700; line-height: 37.5px;
  }
  .genres .last { display: block; padding-left: 130px; }

  .date-box {
    position: absolute; left: 465px; top: 697px; width: 384px; height: 204px;
    background: var(--ink); padding: 20px 0 0 30px; color: var(--white);
  }
  .date-box .lead { font-size: 21px; line-height: 31px; font-weight: 500; }
  .date-box .venue-name { color: var(--hot-pink); font-weight: 600; }
  .date-box .date { color: var(--hot-pink); font-size: 30px; font-weight: 600; line-height: 42px; }
  .date-box .date sup { font-size: 16px; }
  .date-box .time { font-size: 21px; line-height: 30px; font-weight: 500; }

  .address {
    position: absolute; left: 490px; top: 918px;
    color: var(--plum); font-size: 21px; line-height: 28px; font-weight: 400;
  }
  .producers { position: absolute; left: 75px; top: 968px; color: var(--white); }
  .producers .label { font-size: 22px; font-weight: 300; }
  .producers .names { font-size: 27px; font-weight: 800; margin-top: 8px; }

  .footer { position: absolute; left: 0; top: 1058px; width: 849px; height: 142px; }
  .footer-shapes { position: absolute; inset: 0; }
  .more-info { position: absolute; left: 75px; top: 12px; color: var(--white); }
  .more-info .label { font-size: 16px; font-weight: 300; }
  .more-info .url { font-size: 34px; font-weight: 800; margin-top: 6px; }
  .more-info .social { display: flex; align-items: center; gap: 10px; margin-top: 4px; font-size: 16px; font-weight: 400; }
  .more-info .social .mark { width: 15px; height: 15px; background: var(--white); }
  .cash-note {
    position: absolute; left: 585px; top: 54px; color: var(--white);
    font-size: 17px; line-height: 27px; font-weight: 400;
  }
</style>
</head>
<body>
<div class="flyer">
  <header class="launch-band">
    <span class="launch-label">Launching</span>
    <span class="launch-name">TV-VELDA RUSHO</span>
  </header>

  <section class="stage">
    <svg class="crowd-photo" role="img" aria-label="Blurred photo of a dancing club crowd tinted pink" width="849" height="898">
      <defs>
        <linearGradient id="crowdTint" x1="0" y1="0" x2="0" y2="1">
          <stop offset="0" stop-color="#b8139e" stop-opacity="0.35"/>
          <stop offset="0.5" stop-color="#ff40e8" stop-opacity="0.15"/>
          <stop offset="1" stop-color="#a80f92" stop-opacity="0.35"/>
        </linearGradient>
      </defs>
      <rect width="849" height="898" fill="url(#crowdTint)"/>
    </svg>
    <svg class="drummer-art" role="img" aria-label="Illustration of an African woman in silhouette with an afro wrap, seated playing a djembe drum" width="440" height="718">
      <defs>
        <linearGradient id="drummerTone" x1="0" y1="0" x2="1" y2="1">
          <stop offset="0" stop-color="#2a0830" stop-opacity="0.55"/>
          <stop offset="1" stop-color="#3a1250" stop-opacity="0.75"/>
        </linearGradient>
      </defs>
      <rect width="440" height="718" rx="6" fill="url(#drummerTone)"/>
    </svg>
  </section>

  <h1 class="headline">House party!</h1>
  <p class="tagline">New Year<br>New Klubb / New Sounds</p>
  <p class="genres">Bored &amp; Feeling like Grooving<br>to Funkhouse.&nbsp; Dance. Dubstep.<br>Electro.&nbsp; Afro Beat. R n B, Hip Hop.<br>Dancehall. Reggae. Raggaeton. Zouk.<span class="last">Live Bands &amp; Poerty</span></p>

  <div class="date-box">
    <p class="lead"><span class="venue-name">Velda Rusho</span> is the<br>place&nbsp; to be Friday the</p>
    <p class="date">16<sup>th</sup> Jan. 2015</p>
    <p class="time">9pm-3am&nbsp; &amp; every second<br>Friday of the month</p>
  </div>

  <address class="address" style="font-style:normal">@ TOLM<br>Prins Halvard Gate 42,<br>5032 Bergen<br>AGE:18+ KR 100</address>

  <div class="producers">
    <p class="label">Co-produced by:</p>
    <p class="names">A.R.C.O &amp; TOLM</p>
  </div>

  <footer class="footer">
    <svg class="footer-shapes" width="849" height="142" aria-hidden="true">
      <defs>
        <linearGradient id="footLeft" x1="0" y1="0" x2="1" y2="0">
          <stop offset="0" stop-color="#d81cc0"/>
          <stop offset="1" stop-color="#a8108e"/>
        </linearGradient>
        <linearGradient id="footRight" x1="0" y1="0" x2="1" y2="0">
          <stop offset="0" stop-color="#9a1236"/>
          <stop offset="1" stop-color="#5e0a22"/>
        </linearGradient>
      </defs>
      <rect width="849" height="142" fill="url(#footLeft)"/>
      <polygon points="572,0 849,0 849,142 514,142" fill="url(#footRight)"/>
      <polygon points="560,0 572,0 514,142 502,142" fill="#ffffff"/>
    </svg>
    <div class="more-info">
      <p class="label">For more information visit our website:</p>
      <p class="url">www.lorenvisuals.org</p>
      <p class="social"><span class="mark"></span>TV-VELDA RUSHO</p>
    </div>
    <p class="cash-note">DRINKS &amp; FOOD SAVED<br>ON CASH ONLY!!</p>
  </footer>
</div>
</body>
</html>
```